Talbek vodka

With the logo attached in the subsequent file, a business card that reflects a premium and organic vodka. On the first side, the company logo in large. The names must be included on the back of the card (Mateo Ignacio Dalmau Ferrerons with the number +34 655 219 870 and Oriol Batlle Quintana and +34 677 341 592). The slogan "Pure by nature" and "Crafted from organic grain" in bold E-mail (talbekvodka@mailora.net); Website www.talbekvodkaorg.net

```html
<!DOCTYPE html>
<html lang="en">
<head>
<meta charset="utf-8">
<title>Talbek Vodka – Business Card</title>
<link rel="stylesheet" href="https://fonts.googleapis.com/css2?family=Cinzel:wght@400;600;700&display=swap">
<style>
  :root {
    --page-bg: #2b2b2c;
    --card-bg: #fbfbfb;
    --brand-grey: #8b8b8d;
    --text-dark: #555557;
    --name-grey: #6a6a6c;
    --rule-grey: #9a9a9c;
    --icon-grey: #6d6d6f;
  }
  * { box-sizing: border-box; margin: 0; padding: 0; }
  html, body {
    width: 1163px; height: 1200px; overflow: hidden;
    background: var(--page-bg);
    font-family: "Cinzel", "Times New Roman", serif;
  }
  .card {
    position: absolute; left: 91px;
    width: 980px; height: 558px;
    background: var(--card-bg);
    box-shadow: 0 6px 18px rgba(0,0,0,0.45);
  }
  .card--front { top: 28px; }
  .card--back  { top: 614px; }

  /* Front */
  .front-brand {
    position: absolute; left: 0; right: 0; top: 96px;
    text-align: center; color: var(--brand-grey); font-weight: 400;
    line-height: 1;
  }
  .brand-dot {
    display: block; width: 46px; height: 46px; border-radius: 50%;
    background: var(--brand-grey); margin: 0 auto 26px;
  }
  .front-brand .brand-word { display: block; font-size: 132px; letter-spacing: 0.01em; }
  .front-brand .brand-sub  { display: block; font-size: 30px; letter-spacing: 0.3em; margin-top: 6px; padding-left: 0.3em; }
  .front-web {
    position: absolute; left: 0; right: 0; top: 462px;
    text-align: center; color: var(--text-dark);
    font-size: 20px; letter-spacing: 0.36em;
  }

  /* Back */
  .back-identity {
    position: absolute; left: 40px; width: 410px; top: 150px;
    text-align: center;
  }
  .back-brand { color: var(--brand-grey); font-weight: 400; line-height: 1; }
  .back-brand .brand-word { display: block; font-size: 54px; }
  .back-brand .brand-sub  { display: block; font-size: 13px; letter-spacing: 0.3em; margin-top: 3px; }
  .slogan {
    margin-top: 34px; color: var(--brand-grey);
    font-size: 38px; font-weight: 400; letter-spacing: 0.01em; line-height: 1;
  }
  .tagline {
    margin-top: 10px; color: var(--brand-grey);
    font-size: 18px; font-weight: 600; letter-spacing: 0.02em;
  }
  .divider {
    position: absolute; left: 470px; top: 122px; width: 1.5px; height: 282px;
    background: var(--rule-grey);
  }
  .contacts { position: absolute; left: 522px; top: 60px; right: 20px; }
  .person-name {
    color: var(--name-grey); font-weight: 700; font-size: 25px; line-height: 1.3;
  }
  .contact-line {
    display: flex; align-items: center; gap: 14px;
    color: var(--text-dark); font-size: 20px; line-height: 1;
  }
  .contact-line svg { width: 20px; height: 20px; flex: none; }
  .person + .person { margin-top: 36px; }
  .person .contact-line { margin-top: 22px; }
  .web-block { margin-top: 52px; }
  .web-block .contact-line + .contact-line { margin-top: 22px; }
  .web-block .contact-line { font-size: 19px; }
</style>
</head>
<body>
  <section class="card card--front">
    <div class="front-brand">
      <span class="brand-dot"></span>
      <span class="brand-word">TALBEK</span>
      <span class="brand-sub">VODKA</span>
    </div>
    <p class="front-web">WWW.TALBEKVODKAORG.NET</p>
  </section>

  <section class="card card--back">
    <div class="back-identity">
      <div class="back-brand">
        <span class="brand-word">TALBEK</span>
        <span class="brand-sub">VODKA</span>
      </div>
      <p class="slogan">Pure by Nature</p>
      <p class="tagline">Crafted from Organic Grain</p>
    </div>

    <div class="divider"></div>

    <div class="contacts">
      <div class="person">
        <p class="person-name">Mateo Ignacio<br>Dalmau Ferrerons</p>
        <p class="contact-line">
          <svg viewBox="0 0 20 20" aria-hidden="true"><circle cx="10" cy="10" r="10" fill="var(--icon-grey)"/><path d="M7 5.5l1.6-.4 1 2.4-1 .8a6 6 0 0 0 2.8 2.8l.8-1 2.4 1-.4 1.6c-.2.6-.8.9-1.4.8A8 8 0 0 1 6.2 6.9c-.1-.6.2-1.2.8-1.4z" fill="#fff"/></svg>
          +34 655 219 870
        </p>
      </div>
      <div class="person">
        <p class="person-name">Oriol Batlle Quintana</p>
        <p class="contact-line">
          <svg viewBox="0 0 20 20" aria-hidden="true"><circle cx="10" cy="10" r="10" fill="var(--icon-grey)"/><path d="M7 5.5l1.6-.4 1 2.4-1 .8a6 6 0 0 0 2.8 2.8l.8-1 2.4 1-.4 1.6c-.2.6-.8.9-1.4.8A8 8 0 0 1 6.2 6.9c-.1-.6.2-1.2.8-1.4z" fill="#fff"/></svg>
          +34 677 341 592
        </p>
      </div>
      <div class="web-block">
        <p class="contact-line">
          <svg viewBox="0 0 20 20" aria-hidden="true"><circle cx="10" cy="10" r="10" fill="var(--icon-grey)"/><rect x="5" y="6.5" width="10" height="7" rx="1" fill="#fff"/><path d="M5.5 7l4.5 3.5L14.5 7" stroke="var(--icon-grey)" stroke-width="1.2" fill="none"/></svg>
          TALBEKVODKA@MAILORA.NET
        </p>
        <p class="contact-line">
          <svg viewBox="0 0 20 20" aria-hidden="true"><circle cx="10" cy="10" r="10" fill="var(--icon-grey)"/><g stroke="#fff" stroke-width="1.1" fill="none"><circle cx="10" cy="10" r="5.5"/><ellipse cx="10" cy="10" rx="2.4" ry="5.5"/><path d="M4.5 10h11"/></g></svg>
          WWW.TALBEKVODKAORG.NET
        </p>
      </div>
    </div>
  </section>
</body>
</html>
```